Trying to make a small (4.25" x 5.50") re-elect sticker for a congressman in california. The congressmans name is Calder Voss and we would like to change his last name to "Vossovich". Basically we believe his relationship to Pike/Brevik should be reflected in this poster with russia undertones.

The idea behind this project is to reflect Calder Voss as a political puppet of Harlan Pike who is also a puppet of Russian president Brevik.
We do not support Calder Voss as our elected official and believe him to be a traitor to our district and a traitor to our country.
Trying to make a small (4.25" x 5.50") re-elect sticker for a congressman in California. The congressman's name is Calder Voss and we would like to change his last name to "Vossovich". Basically we believe his relationship to Pike/Brevik should be reflected in this poster with Russia undertones.

Trying to make a small (4.25" x 5.50") re-elect sticker for a congressman in California. The congressman's name is Calder Voss and we would like to change his last name to "Vossovich". Basically we believe his relationship to Pike/Brevik should be reflected in this poster with Russian undertones.

I have never done this type of project before so any advise would be helpful,any questions just email me thanks.
Owen

Owen

Target Market(s)

For political grass roots campaign.

Industry/Entity Type

Political

Colors

Designer to choose colors to be used in the design.

Requirements
Must have
• Picture of Calder Voss. Re-elect (переизбрание). Change last name to Vossovich
Nice to have
• Maybe the hammer and sickle logo someplace but not too obvious
Should not have
• Nothing obscene or offensiveпереизбрание

```html
<!DOCTYPE html>
<html lang="en">
<head>
<meta charset="utf-8">
<title>Re-Elect Calder Vossovich</title>
<link rel="stylesheet" href="https://fonts.googleapis.com/css2?family=Playfair+Display:wght@800&family=Merriweather:wght@900&family=Montserrat:wght@600;700&display=swap">
<style>
  :root {
    --blue: #0a12d6;
    --navy: #00007e;
    --red: #b40000;
    --grey: #c9c9c9;
    --white: #ffffff;
    --flag-light: #f4a6a2;
    --flag-mid: #e9807b;
    --flag-deep: #d9625e;
    --emblem-gold: #f1d58a;
    --suit-dark: #3a2a30;
    --frame-edge: #f08c86;
  }
  * { margin: 0; padding: 0; box-sizing: border-box; }
  html, body { width: 1200px; height: 927px; overflow: hidden; background: var(--white); }
  .sticker { position: relative; width: 1200px; height: 927px; }
  .band-top { position: absolute; left: 0; top: 0; width: 1200px; height: 85px; background: var(--blue); }
  .portrait {
    position: absolute; left: 0; top: 85px; width: 428px; height: 650px;
    border-right: 2px solid var(--frame-edge);
    background:
      radial-gradient(ellipse 260px 200px at 90px 120px, rgba(241, 213, 138, 0.55), rgba(241, 213, 138, 0) 70%),
      radial-gradient(ellipse 340px 240px at 230px 650px, rgba(58, 42, 48, 0.75), rgba(58, 42, 48, 0) 75%),
      linear-gradient(160deg, var(--flag-light) 0%, var(--flag-mid) 30%, var(--flag-deep) 50%, var(--flag-mid) 70%, var(--flag-light) 100%);
  }
  .panel { position: absolute; left: 428px; top: 85px; width: 772px; height: 650px; background: var(--grey); }
  .headline {
    position: absolute; left: 428px; top: 151px; width: 762px; text-align: center;
    font-family: "Playfair Display", Georgia, serif; font-weight: 800; font-size: 140px;
    color: var(--blue); line-height: 1;
  }
  .ribbon { position: absolute; left: 0; top: 0; }
  .ribbon-text {
    position: absolute; left: 470px; top: 300px; width: 693px; text-align: center;
    font-family: "Montserrat", Arial, sans-serif; font-weight: 700; font-size: 74px;
    color: var(--white); line-height: 100px;
  }
  .first-name {
    position: absolute; left: 488px; top: 427px;
    font-family: "Montserrat", Arial, sans-serif; font-weight: 600; font-size: 112px;
    color: var(--blue); letter-spacing: 4px; line-height: 1;
  }
  .last-name {
    position: absolute; left: 486px; top: 559px;
    font-family: "Montserrat", Arial, sans-serif; font-weight: 700; font-size: 104px;
    color: var(--red); line-height: 1;
  }
  .tagline {
    position: absolute; left: 0; top: 735px; width: 1200px; height: 107px;
    display: flex; align-items: center; justify-content: center;
    font-family: "Merriweather", Georgia, serif; font-weight: 900; font-size: 50px; color: var(--blue);
    background: var(--white);
  }
  .band-bottom { position: absolute; left: 0; top: 842px; width: 1200px; height: 85px; background: var(--red); }
</style>
</head>
<body>
<main class="sticker">
  <div class="band-top"></div>
  <div class="portrait" role="img" aria-label="Head-and-shoulders portrait photo of the congressman in a dark suit and striped tie, smiling, in front of a waving red flag with a gold emblem in the upper left"></div>
  <div class="panel"></div>
  <h1 class="headline">RE-ELECT</h1>
  <svg class="ribbon" width="1200" height="927" viewBox="0 0 1200 927" aria-hidden="true">
    <polygon points="925,412 1163,412 1160,418 925,480" fill="var(--navy)"/>
    <polygon points="452,293 1163,293 1163,412 452,412 500,352" fill="var(--blue)"/>
  </svg>
  <p class="ribbon-text" lang="ru">переизбрание</p>
  <p class="first-name">Calder</p>
  <p class="last-name">VOSSOVICH</p>
  <p class="tagline">Imagine what this guy could do!</p>
  <div class="band-bottom"></div>
</main>
</body>
</html>
```